Design a nice single page website containing a link list

Hello,

you should design a nice single page website to replace the old website http://www.tovrella.de/

The company is running multiple flag shops. Your new website should only lead to a lot of other company websites. They are mentioned below. No link dropdowns please. We would like to see all links.

The company is offering flags. Big flags, but the special products are high quality diplomatic car flags. It is important, that people see, that it is about flags and specialy about car flags.

As customers are very international, the website should not contain unnecessary text. No text, no wrong languages.

You should implement links to:

Car Flag Shops: (pleaae don't use this as headline. Use symbols)
New Logo: Little car attached (without text below)
http://www.ridepennon.eu (english site payment in Euro)
http://us.ridepennon.eu (english site payment in USD)
http://fr.ridepennon.eu (french site payment in Euro)
http://es.ridepennon.eu (spanish site payment in Euro)
http://de.ridepennon.eu (germansite payment in Euro)

http://www.ridepennon.net (english site payment in USD)
http://www.ridepennant.co.uk (english site payment in british pounds)
http://www.wagen-wimpel.net (german site payment in Euro)
http://www.wagen-banner.at (austrian site payment in Euro)
http://www.wagen-wimpl.ch (german site payment in Swiss Franken)

Big flag shops: (pleaae don't use this as headline. Use symbols)
Logo: tovRella (attached incl. font) (black part of logo can also be made white)
(World map used next to the tovRella font attached)
http://www.tovrella.ne/ (english site payment in Euro)
http://fr.tovrella.net (french site payment in Euro)
http://es.tovrella.net (spanish site payment in Euro)
http://de.tovrella.net (german site payment in Euro)
http://it.tovrella.net (italian site payment in Euro)

Car flags product page: (pleaae don't use this as headline. Use symbols)
Logo: EnvoyPennon (attached incl. font)
http://www.envoy-pennon.com (english site)
http://fr.envoy-pennon.com (french site)
http://es.envoy-pennon.com (spanish site)
http://de.envoy-pennon.com (german site)

Please also add links to
English Blog
German Blog
4 language newsletter registration forms.

Also company data has to be added to the bottom of the page.
You could copy / paste from here:
http://www.ridepennon.eu/tovRella-GmbH

No additional links. No social icons.

General design:
Customers are, ambassoders, embassies, international organisiations.
Customers are powerful men, who want to show their power.
That's the reason, why they add this car flags to their car.

So colors should not be too soft. In the past we used colors like black and gold.
Completly black / dark background and bright white text is ok.

Most of our company prints have the kelvane arch in the background.
It would be good to include this also. (Image attached)

It is about a flag company. So don't forget to add big flags.
It would be also good to include an image like this:
http://de.pixvendra.com/id/38275016

Logos are available in high resolution. At the end you should mail us psd file with your winning design.

Please feel free to use all images you will find on the websites above.
If you need special images, please let me know, and we willt try to provide them.

Kind regards,

Dorian
Updates

Hello,
thanks for your feedback.Project payment is now committed.
Kind regards,
Lorenzo

Target Market(s)

World wide

Industry/Entity Type

Flag

Requirements
Must have
• Self explaining links to all the target pages.
Should not have
• unnecessary text. Domain names and logos with text are fine.
I think, we could avoid nearly all other text.

```html
<!DOCTYPE html>
<html lang="en">
<head>
<meta charset="utf-8">
<title>tovRella – Flag Shops</title>
<link href="https://fonts.googleapis.com/css2?family=Roboto+Condensed:wght@300;400;700&family=Roboto:wght@400;500&display=swap" rel="stylesheet">
<style>
  :root{
    --ink:#1a1a1a;
    --header:#141414;
    --white:#ffffff;
    --muted:#8a8a8a;
    --text:#555555;
    --rule:#d6d6d6;
    --band:#ececec;
    --gold:#8c6d2c;
    --grey-logo:#a9a9a9;
  }
  *{box-sizing:border-box;margin:0;padding:0}
  html,body{width:1200px;height:1079px;overflow:hidden;background:var(--white);font-family:"Roboto",Arial,sans-serif}
  .page{position:relative;width:1200px;height:1079px}

  .hero{position:absolute;left:0;top:0;width:1200px;height:613px;overflow:hidden}
  .hero__photo{position:absolute;inset:0;
    background:
      radial-gradient(ellipse at 50% 45%, rgba(0,0,0,0) 30%, rgba(0,0,0,.65) 100%),
      linear-gradient(100deg,#7a2a26 0%,#e9e4e0 12%,#2f3f7d 22%,#b8b2b0 30%,#8c2a24 40%,#3f7a45 48%,#d8d2cc 56%,#9a2d25 64%,#2b3a72 74%,#c9c3c0 82%,#7b2520 92%,#2a2f55 100%);
    filter:saturate(.8)}
  .hero__shade{position:absolute;inset:0;background:rgba(0,0,0,.35)}

  .topbar{position:absolute;left:0;top:0;width:1200px;height:108px;background:rgba(18,18,18,.93)}
  .topbar__left{position:absolute;left:140px;top:38px;display:flex;align-items:center;gap:6px}
  .topbar__right{position:absolute;left:983px;top:38px;display:flex;align-items:center;gap:6px}
  .flag{display:inline-block;width:14px;height:9px}
  .brand{position:absolute;left:0;right:0;top:24px;text-align:center;font-family:"Roboto Condensed",Arial,sans-serif;font-weight:700;font-size:46px;color:#9a9a9a;letter-spacing:1px}

  .welcome{position:absolute;left:0;top:262px;width:1200px;text-align:center;color:var(--white)}
  .welcome__title{display:flex;align-items:center;justify-content:center;gap:36px;font-family:"Roboto Condensed",Arial,sans-serif;font-weight:300;font-size:44px;line-height:50px}
  .welcome__title::before,.welcome__title::after{content:"";width:220px;height:1px;background:var(--white)}
  .welcome__text{margin-top:12px;font-size:15.5px;line-height:24px}
  .welcome__text p+p{margin-top:21px}

  .shops{position:absolute;left:140px;top:655px;width:920px;height:160px;border-bottom:1px solid var(--rule);display:flex}
  .shop{position:relative;height:100%;text-align:center}
  .shop+.shop{border-left:1px solid var(--rule)}
  .shop:nth-child(1){width:304px}
  .shop:nth-child(2){width:315px}
  .shop:nth-child(3){width:301px}
  .shop__logo{position:absolute;left:0;right:0;top:48px;height:50px;display:flex;align-items:center;justify-content:center;gap:10px}
  .shop__url{position:absolute;left:0;right:0;top:128px;font-size:13.5px;color:var(--muted)}
  .logo-envoy{font-family:"Roboto Condensed",Arial,sans-serif;font-size:34px;font-weight:400;color:var(--gold);letter-spacing:1px}
  .logo-ride{font-family:"Roboto Condensed",Arial,sans-serif;font-size:36px;font-weight:700;color:var(--ink)}
  .logo-tov{font-family:"Roboto Condensed",Arial,sans-serif;font-size:40px;font-weight:700;color:var(--grey-logo)}
  .mark-circle{width:26px;height:26px;border-radius:50%;background:var(--ink)}

  .domains{position:absolute;left:140px;top:855px;width:920px;height:70px;background:var(--band);text-align:center;font-size:12.5px;color:var(--text)}
  .domains__list{padding-top:16px}
  .domains__list span+span::before{content:"|";margin:0 7px;color:#888}
  .domains__cur{position:absolute;top:44px;left:0;width:100%;font-weight:500;color:#333}
  .cur{position:absolute;display:flex;align-items:center;gap:6px;white-space:nowrap}
  .cur .flag{width:14px;height:9px}

  .footer-links{position:absolute;left:0;top:948px;width:1200px;text-align:center;font-size:12.5px;color:var(--text)}
  .footer-links span+span::before{content:"|";margin:0 7px}
  .footer-note{position:absolute;left:0;top:991px;width:1200px;text-align:center;font-size:12px;color:var(--text)}
  .footer-copy{position:absolute;left:0;top:1015px;width:1200px;text-align:center;font-size:11.5px;color:var(--text)}
</style>
</head>
<body>
<div class="page">
  <section class="hero">
    <div class="hero__photo" role="img" aria-label="Blurred photograph of many national flags hanging side by side"></div>
    <div class="hero__shade"></div>

    <header class="topbar">
      <div class="topbar__left">
        <svg width="28" height="22" viewBox="0 0 28 22" aria-label="Newsletter"><rect x="1" y="6" width="26" height="15" fill="#bdbdbd"/><path d="M1 6 L14 15 L27 6" fill="none" stroke="#555" stroke-width="1.2"/><path d="M3 6 L14 0 L25 6" fill="#9d9d9d"/></svg>
        <svg class="flag" viewBox="0 0 14 9"><rect width="14" height="3" fill="#111"/><rect y="3" width="14" height="3" fill="#d00"/><rect y="6" width="14" height="3" fill="#fc0"/></svg>
        <svg class="flag" viewBox="0 0 14 9"><rect width="14" height="9" fill="#c8102e"/><rect x="6" width="2" height="9" fill="#fff"/><rect y="3.5" width="14" height="2" fill="#fff"/></svg>
        <svg class="flag" viewBox="0 0 14 9"><rect width="5" height="9" fill="#0050a4"/><rect x="5" width="4" height="9" fill="#fff"/><rect x="9" width="5" height="9" fill="#ef4135"/></svg>
        <svg class="flag" viewBox="0 0 14 9"><rect width="14" height="9" fill="#c60b1e"/><rect y="2.5" width="14" height="4" fill="#ffc400"/></svg>
      </div>
      <div class="brand">tovRella</div>
      <div class="topbar__right">
        <svg width="32" height="22" viewBox="0 0 32 22" aria-label="Blog"><ellipse cx="12" cy="9" rx="11" ry="8" fill="#bdbdbd"/><path d="M5 14 L3 20 L10 16Z" fill="#bdbdbd"/><ellipse cx="22" cy="12" rx="9" ry="6.5" fill="#d8d8d8"/><path d="M27 16 L30 21 L23 18Z" fill="#d8d8d8"/></svg>
        <svg class="flag" viewBox="0 0 14 9"><rect width="14" height="3" fill="#111"/><rect y="3" width="14" height="3" fill="#d00"/><rect y="6" width="14" height="3" fill="#fc0"/></svg>
        <svg class="flag" viewBox="0 0 14 9"><rect width="14" height="9" fill="#c8102e"/><rect x="6" width="2" height="9" fill="#fff"/><rect y="3.5" width="14" height="2" fill="#fff"/></svg>
      </div>
    </header>

    <div class="welcome">
      <h1 class="welcome__title">Welcome</h1>
      <div class="welcome__text">
        <p>Lorem Ipsum is simply dummy text of the printing and typesetting industry. Lorem Ipsum has been the industry's<br>standard dummy text ever since the 1500s.</p>
        <p>When an unknown printer took a galley of type and scrambled it to make a type specimen book.<br>It has survived not only five centuries, but also the leap into electronic typesetting.</p>
      </div>
    </div>
  </section>

  <section class="shops">
    <div class="shop">
      <div class="shop__logo"><span class="logo-envoy">EnvoyPennon</span></div>
      <div class="shop__url">http://www.envoy-pennon.com/</div>
    </div>
    <div class="shop">
      <div class="shop__logo"><span class="logo-ride">ridepennon.eu</span></div>
      <div class="shop__url">http://www.ridepennon.eu/</div>
    </div>
    <div class="shop">
      <div class="shop__logo"><span class="logo-tov">tovRella</span></div>
      <div class="shop__url">http://www.tovrella.de/</div>
    </div>
  </section>

  <section class="domains">
    <div class="domains__list">
      <span>www.ridepennon.eu</span><span>www.ridepennon.net</span><span>www.ridepennant.co.uk</span><span>www.wagen-wimpel.net</span><span>www.wagen-banner.at</span><span>www.wagen-wimpl.ch</span>
    </div>
    <div class="domains__cur">
      <div class="cur" style="left:93px">Deutsch <svg class="flag" viewBox="0 0 14 9"><rect width="14" height="9" fill="#1f3a93"/><circle cx="7" cy="4.5" r="2.5" fill="none" stroke="#fc0" stroke-width=".8"/></svg> €</div>
      <div class="cur" style="left:216px">English <svg class="flag" viewBox="0 0 14 9"><rect width="14" height="9" fill="#b22234"/><rect y="2" width="14" height="1.3" fill="#fff"/><rect y="4.6" width="14" height="1.3" fill="#fff"/><rect width="6" height="4.6" fill="#3c3b6e"/></svg> $</div>
      <div class="cur" style="left:336px">English <svg class="flag" viewBox="0 0 14 9"><rect width="14" height="9" fill="#012169"/><path d="M0 0L14 9M14 0L0 9" stroke="#fff" stroke-width="1.6"/><rect x="6" width="2" height="9" fill="#c8102e"/><rect y="3.5" width="14" height="2" fill="#c8102e"/></svg> £</div>
      <div class="cur" style="left:472px">USA <svg class="flag" viewBox="0 0 14 9"><rect width="14" height="9" fill="#b22234"/><rect y="2" width="14" height="1.3" fill="#fff"/><rect y="4.6" width="14" height="1.3" fill="#fff"/><rect width="6" height="4.6" fill="#3c3b6e"/></svg> $</div>
      <div class="cur" style="left:592px">Australia <svg class="flag" viewBox="0 0 14 9"><rect width="14" height="9" fill="#b22234"/><rect y="2" width="14" height="1.3" fill="#fff"/><rect y="4.6" width="14" height="1.3" fill="#fff"/><rect width="6" height="4.6" fill="#3c3b6e"/></svg> A$</div>
      <div class="cur" style="left:727px">German <svg class="flag" viewBox="0 0 14 9"><rect width="14" height="9" fill="#d52b1e"/><rect x="6" y="1.5" width="2" height="6" fill="#fff"/><rect x="4" y="3.5" width="6" height="2" fill="#fff"/></svg> Fr</div>
    </div>
  </section>

  <nav class="footer-links">
    <span>Home</span><span>Customer Service</span><span>Impressum</span><span>Site Map</span><span>Search Terms</span><span>Advanced Search</span><span>Orders &amp; Returns</span><span>Contact Us</span><span>RSS</span>
  </nav>
  <p class="footer-note">Help Us to Keep Storevine Healthy - Report All Bugs (ver. 1.7.0.2)</p>
  <p class="footer-copy">© 2013 tovRella GmbH</p>
</div>
</body>
</html>
```